Business card for STEADYWAVE

Please design professional business card for IT consulting firm STEADYWAVE INC.
Use logo attached.
Use information from sample qNode business card attached.
replace qnode inc with STEADYWAVE INC.
as well as qnodeinc.com with steadywave.example

```html
<!DOCTYPE html>
<html lang="en">
<head>
<meta charset="utf-8">
<title>STEADYWAVE business card</title>
<link rel="stylesheet" href="https://fonts.googleapis.com/css2?family=Montserrat:wght@400;500;700&display=swap">
<style>
  :root {
    --bg: #b9b9b9;
    --card: #ffffff;
    --ink: #111111;
    --text: #2b2b2b;
    --purple: #7d3f98;
    --teal: #6fc7b1;
    --orange: #f5951f;
    --blue: #62c6e8;
    --rule: #f6a93b;
  }
  * { box-sizing: border-box; margin: 0; padding: 0; }
  html, body { width: 1200px; height: 815px; overflow: hidden; }
  body {
    background: var(--bg);
    font-family: "Montserrat", sans-serif;
    position: relative;
  }
  .card {
    position: absolute;
    left: 100px; top: 122px;
    width: 1000px; height: 571px;
    background: var(--card);
    border-radius: 34px;
    overflow: hidden;
    box-shadow: 0 14px 30px rgba(0,0,0,0.25);
  }
  .brand {
    position: absolute;
    left: 62px; top: 96px;
    display: flex; align-items: center; gap: 18px;
  }
  .brand-name {
    font-weight: 700;
    font-size: 78px;
    letter-spacing: 0.07em;
    color: var(--ink);
    line-height: 1;
  }
  .brand-mark {
    width: 22px; height: 22px;
    background: var(--purple);
    align-self: flex-start;
  }
  .person { position: absolute; left: 64px; top: 262px; }
  .person-name {
    font-weight: 700; font-size: 34px; color: var(--purple);
    letter-spacing: 0.02em; line-height: 1.1;
  }
  .person-title {
    font-weight: 500; font-size: 24px; color: var(--text);
    letter-spacing: 0.03em; margin-top: 2px;
  }
  .rule {
    position: absolute; left: 64px; top: 352px;
    width: 860px; height: 2px; background: var(--rule);
  }
  .contacts {
    position: absolute; left: 64px; top: 380px;
    list-style: none;
  }
  .contacts li {
    display: flex; align-items: center; gap: 12px;
    font-size: 23px; font-weight: 500; color: var(--ink);
    line-height: 33px;
  }
  .contacts svg { width: 17px; height: 17px; flex: none; }
  .company {
    position: absolute; right: 62px; top: 398px;
    text-align: right;
  }
  .company-name {
    font-weight: 700; font-size: 25px; color: var(--purple);
    letter-spacing: 0.03em;
  }
  .company-address {
    font-size: 22px; font-weight: 500; color: var(--ink);
    line-height: 30px; margin-top: 4px;
  }
  .base-band {
    position: absolute; left: 0; bottom: 0;
    width: 100%; height: 14px;
    background: var(--purple);
  }
</style>
</head>
<body>
  <article class="card">
    <div class="brand">
      <span class="brand-name">STEADYWAVE</span>
      <span class="brand-mark"></span>
    </div>

    <div class="person">
      <p class="person-name">DANIEL MORROW</p>
      <p class="person-title">GENERAL MANAGER</p>
    </div>

    <div class="rule"></div>

    <ul class="contacts">
      <li>
        <svg viewBox="0 0 20 20"><path fill="#7d3f98" d="M5 2l3 4-2 2c1 2 3 4 5 5l2-2 4 3-2 3C9 17 3 11 2 5z"/></svg>
        (555) 201-4470 ext.318
      </li>
      <li>
        <svg viewBox="0 0 20 20"><path fill="#6fc7b1" d="M5 2l3 4-2 2c1 2 3 4 5 5l2-2 4 3-2 3C9 17 3 11 2 5z"/></svg>
        (555) 384-9012
      </li>
      <li>
        <svg viewBox="0 0 20 20"><rect x="2" y="4" width="16" height="12" fill="#62c6e8"/><path d="M2 4l8 7 8-7" fill="none" stroke="#fff" stroke-width="1.6"/></svg>
        dmorrow@steadywave.example
      </li>
      <li>
        <svg viewBox="0 0 20 20"><circle cx="10" cy="10" r="8" fill="#f5951f"/><path d="M2 10h16M10 2c-3 3-3 13 0 16M10 2c3 3 3 13 0 16" fill="none" stroke="#fff" stroke-width="1.2"/></svg>
        www.steadywave.example
      </li>
    </ul>

    <div class="company">
      <p class="company-name">STEADYWAVE INC.</p>
      <p class="company-address">1280 Harbour Lane, Suite 460<br>Northfield, Ontario, A1B 2C3, Canada</p>
    </div>

    <div class="base-band"></div>
  </article>
</body>
</html>
```